Prescripton Pad for Mental health professionals and life wellness coaches

I need a note pad designed for therapist and coaches that will allow us to write our client homework just like a doctor would write out a prescription for medication.(i.e read for chapter of book, or 30 minutes of mediation a day, etc.). I would like to see sections for stuff to ponder, as well as action to take. Something that has the seriousness of a doctor pad but also some sleep professional twist to it. I would like for these to be sold where businesses can add in their own names and logos at the top.

Target Market(s)

Mental Health Professionals, Psychiatrist, Life coaches, Wellness Coaches

Industry/Entity Type

Mental Health

Font styles to use
Script

Requirements
Must have
• Space for individuals to add in their own name a logos
• Look of a prescription pad from the doctor
• Some sleek, unique aspect to it
Nice to have
• Section with boxed that can be checked such as :mindfulness, Meditation, cardio, strength training, massage, date night, Sleep _ hours

```html
<!DOCTYPE html>
<html lang="en">
<head>
<meta charset="utf-8">
<title>Quiet Harbor Clinic – Prescription Pad</title>
<link href="https://fonts.googleapis.com/css2?family=Ubuntu:wght@400;500;700&display=swap" rel="stylesheet">
<style>
  :root {
    --page: #ece6de;
    --paper: #ffffff;
    --ink: #4a4a4a;
    --ink-strong: #3f3f3f;
    --rule: #6d6d6d;
    --blue: #1f75be;
    --green: #8cc63f;
    --orange: #f7931e;
    --purple: #662d91;
  }
  * { box-sizing: border-box; margin: 0; padding: 0; }
  html, body {
    width: 1200px; height: 1200px; overflow: hidden;
    background: var(--page);
    font-family: "Ubuntu", sans-serif;
    color: var(--ink);
  }
  .sheet-stack {
    position: relative; width: 1200px; height: 1200px;
  }
  .pad {
    position: absolute; left: 180px;
    width: 840px; height: 545px;
    background: var(--paper);
    box-shadow: 0 3px 8px rgba(0,0,0,0.25);
    overflow: hidden;
  }
  .pad--blue { top: 32px; --band: var(--blue); --accent: var(--green); --brand: var(--blue); }
  .pad--orange { top: 610px; --band: var(--orange); --accent: var(--purple); --brand: var(--purple); }

  .pad__header { position: absolute; left: 0; top: 0; width: 840px; height: 160px; }
  .pad__band { fill: var(--band); }
  .pad__stripe { fill: var(--accent); }

  .clinic-info {
    position: absolute; left: 544px; top: 20px;
    color: #fff; font-size: 15px; line-height: 17.5px;
  }
  .clinic-info__name { font-size: 20px; font-weight: 700; line-height: 24px; }

  .brand {
    position: absolute; left: 72px; top: 66px;
    display: flex; align-items: center; gap: 10px;
    color: var(--brand); font-size: 22px; font-weight: 700;
  }
  .brand__dot {
    width: 18px; height: 18px; border-radius: 50%;
    background: var(--accent);
  }

  .patient-fields {
    position: absolute; left: 44px; top: 128px;
    font-size: 18px; line-height: 25px; color: var(--ink);
  }
  .patient-fields__row { display: flex; }
  .patient-fields__label { width: 104px; }

  .rx-mark {
    position: absolute; left: 44px; top: 194px;
    font-size: 34px; font-weight: 700; color: var(--ink);
    letter-spacing: -1px;
  }
  .rx-mark small { font-size: 22px; font-weight: 500; vertical-align: 12px; }

  .order { position: absolute; left: 542px; top: 202px; }
  .order__title { font-size: 20px; font-weight: 500; color: var(--ink-strong); margin-bottom: 9px; }
  .order__list { list-style: none; }
  .order__item {
    display: flex; align-items: center;
    height: 25.8px; font-size: 14px; font-weight: 500; color: var(--ink-strong);
  }
  .order__box {
    width: 14px; height: 14px; border: 1px solid var(--ink);
    margin-right: 9px; flex: none;
  }
  .order__blank {
    display: inline-block; width: 54px; border-bottom: 1px solid var(--ink);
    margin: 0 8px 0 4px; transform: translateY(4px);
  }
  .order__blank--wide { margin-left: 10px; margin-right: 12px; }

  .signature {
    position: absolute; left: 44px; top: 496px;
    display: flex; align-items: flex-end;
    font-size: 19px; font-weight: 500; color: var(--ink-strong);
  }
  .signature__line {
    width: 238px; border-bottom: 1px solid var(--rule);
    margin-left: 22px; margin-bottom: 3px;
  }
</style>
</head>
<body>
<main class="sheet-stack">

  <section class="pad pad--blue">
    <svg class="pad__header" viewBox="0 0 840 160" aria-hidden="true">
      <path class="pad__stripe" d="M180,0 H840 V60 C810,128 720,145 585,142 C430,135 330,20 200,8 Z"/>
      <path class="pad__band" d="M0,0 H840 V40 C815,110 720,132 585,128 C430,124 330,10 200,3 C110,-2 40,30 0,70 Z"/>
    </svg>
    <div class="clinic-info">
      <div class="clinic-info__name">Quiet Harbor Clinic</div>
      <div>Street 1, address information1</div>
      <div>phone number - email@email.com</div>
      <div>www.quietharborclinic.com</div>
    </div>
    <div class="brand"><span class="brand__dot"></span><span>QUIET HARBOR CLINIC</span></div>
    <div class="patient-fields">
      <div class="patient-fields__row"><span class="patient-fields__label">Patient</span><span>:</span></div>
      <div class="patient-fields__row"><span class="patient-fields__label">Physician</span><span>:</span></div>
    </div>
    <div class="rx-mark">R<small>x</small></div>
    <div class="order">
      <div class="order__title">Order</div>
      <ul class="order__list">
        <li class="order__item"><span class="order__box"></span>Sleep<span class="order__blank"></span>hrs/day</li>
        <li class="order__item"><span class="order__box"></span>Mediation<span class="order__blank order__blank--wide"></span>hrs/day</li>
        <li class="order__item"><span class="order__box"></span>Cardio</li>
        <li class="order__item"><span class="order__box"></span>Massage</li>
        <li class="order__item"><span class="order__box"></span>Self Care</li>
        <li class="order__item"><span class="order__box"></span>Reading books</li>
        <li class="order__item"><span class="order__box"></span>Balance Training</li>
        <li class="order__item"><span class="order__box"></span>Home Exercise</li>
        <li class="order__item"><span class="order__box"></span>Strength training</li>
        <li class="order__item"><span class="order__box"></span>others :</li>
      </ul>
    </div>
    <div class="signature">Physician Signature<span class="signature__line"></span></div>
  </section>

  <section class="pad pad--orange">
    <svg class="pad__header" viewBox="0 0 840 160" aria-hidden="true">
      <path class="pad__stripe" d="M180,0 H840 V60 C810,128 720,145 585,142 C430,135 330,20 200,8 Z"/>
      <path class="pad__band" d="M0,0 H840 V40 C815,110 720,132 585,128 C430,124 330,10 200,3 C110,-2 40,30 0,70 Z"/>
    </svg>
    <div class="clinic-info">
      <div class="clinic-info__name">Quiet Harbor Clinic</div>
      <div>Street 1, address information1</div>
      <div>phone number - email@email.com</div>
      <div>www.quietharborclinic.com</div>
    </div>
    <div class="brand"><span class="brand__dot"></span><span>QUIET HARBOR CLINIC</span></div>
    <div class="patient-fields">
      <div class="patient-fields__row"><span class="patient-fields__label">Patient</span><span>:</span></div>
      <div class="patient-fields__row"><span class="patient-fields__label">Physician</span><span>:</span></div>
    </div>
    <div class="rx-mark">R<small>x</small></div>
    <div class="order">
      <div class="order__title">Order</div>
      <ul class="order__list">
        <li class="order__item"><span class="order__box"></span>Sleep<span class="order__blank"></span>hrs/day</li>
        <li class="order__item"><span class="order__box"></span>Mediation<span class="order__blank order__blank--wide"></span>hrs/day</li>
        <li class="order__item"><span class="order__box"></span>Cardio</li>
        <li class="order__item"><span class="order__box"></span>Massage</li>
        <li class="order__item"><span class="order__box"></span>Self Care</li>
        <li class="order__item"><span class="order__box"></span>Reading books</li>
        <li class="order__item"><span class="order__box"></span>Balance Training</li>
        <li class="order__item"><span class="order__box"></span>Home Exercise</li>
        <li class="order__item"><span class="order__box"></span>Strength training</li>
        <li class="order__item"><span class="order__box"></span>others :</li>
      </ul>
    </div>
    <div class="signature">Physician Signature<span class="signature__line"></span></div>
  </section>

</main>
</body>
</html>
```